Business card for a business coach / management consultant

My logo has been done and now I need a business card. Deliverable needs to be a PDF to give to the printer. I want it single sided as I want the back side blank.
I prefer a white card with modern simple professional design.
Details are:
Dale Whitford
B.Sc. (hons) FRLT CP MNBQR
7 Corrigan Rd
Kestrel Bay WA 6091
Australia
mobile 040 31 582 47
email dale@ventureharbor.example.au
skype dalewhitfordnorth
Small to medium size business owners
Business

```html
<!DOCTYPE html>
<html lang="en">
<head>
<meta charset="utf-8">
<title>Dale Whitford – Business Card</title>
<link rel="stylesheet" href="https://fonts.googleapis.com/css2?family=Montserrat:wght@700;800&family=Source+Sans+3:wght@400&display=swap">
<style>
  :root {
    --backdrop: #c9cfcd;
    --card: #ffffff;
    --brand-blue: #1b2f9e;
    --text-blue: #1b2f9e;
    --icon-fg: #ffffff;
  }
  * { margin: 0; padding: 0; box-sizing: border-box; }
  html, body {
    width: 1200px;
    height: 1000px;
    overflow: hidden;
    background: var(--backdrop);
  }
  .card {
    position: absolute;
    left: 150px;
    top: 225px;
    width: 900px;
    height: 550px;
    background: var(--card);
    box-shadow: 0 6px 18px rgba(0,0,0,0.12);
  }
  .holder-name {
    position: absolute;
    left: 62px;
    top: 190px;
    font-family: "Montserrat", sans-serif;
    font-weight: 800;
    font-size: 60px;
    letter-spacing: 0.5px;
    color: var(--text-blue);
    line-height: 1;
    white-space: nowrap;
  }
  .credentials {
    position: absolute;
    left: 64px;
    top: 262px;
    font-family: "Montserrat", sans-serif;
    font-weight: 700;
    font-size: 17px;
    letter-spacing: 0.6px;
    color: var(--text-blue);
    white-space: nowrap;
  }
  .contact {
    position: absolute;
    left: 64px;
    font-family: "Source Sans 3", sans-serif;
    font-size: 20px;
    line-height: 26px;
    color: var(--text-blue);
    white-space: nowrap;
  }
  .contact-address { top: 300px; }
  .contact-direct { top: 396px; }
  .contact-row {
    display: flex;
    align-items: center;
    gap: 16px;
  }
  .contact-icon {
    width: 20px;
    height: 20px;
    flex: none;
  }
  .address-block {
    display: flex;
    gap: 16px;
  }
  .address-block .contact-icon { margin-top: 3px; }
  .brand {
    position: absolute;
    left: 560px;
    top: 205px;
    display: flex;
    align-items: center;
    gap: 14px;
    white-space: nowrap;
  }
  .brand-mark {
    width: 46px;
    height: 46px;
    flex: none;
    border-radius: 50%;
    background: var(--brand-blue);
  }
  .brand-name {
    font-family: "Montserrat", sans-serif;
    font-weight: 800;
    font-size: 30px;
    color: var(--brand-blue);
    line-height: 1;
  }
  .band {
    position: absolute;
    left: 0;
    right: 0;
    bottom: 18px;
    height: 38px;
    background: var(--brand-blue);
  }
</style>
</head>
<body>
  <div class="card">
    <div class="holder-name">Dale Whitford</div>
    <div class="credentials">B.Sc. (hons) FRLT CP MNBQR</div>

    <div class="contact contact-address">
      <div class="address-block">
        <svg class="contact-icon" viewBox="0 0 20 20" aria-hidden="true">
          <rect width="20" height="20" fill="var(--brand-blue)"/>
          <path d="M10 4 L16 10 H14 V16 H6 V10 H4 Z" fill="var(--icon-fg)"/>
        </svg>
        <div>7 Corrigan Rd<br>Kestrel Bay WA 6091<br>Australia</div>
      </div>
    </div>

    <div class="contact contact-direct">
      <div class="contact-row">
        <svg class="contact-icon" viewBox="0 0 20 20" aria-hidden="true">
          <rect width="20" height="20" fill="var(--brand-blue)"/>
          <path d="M6 4 L9 4 L9 7 L7.5 8.5 Q9 12 11.5 12.5 L13 11 L16 11 L16 14 Q15 16 13 16 Q5 14 4 6 Q4 4 6 4 Z" fill="var(--icon-fg)"/>
        </svg>
        <span>040 31 582 47</span>
      </div>
      <div class="contact-row">
        <svg class="contact-icon" viewBox="0 0 20 20" aria-hidden="true">
          <rect width="20" height="20" fill="var(--brand-blue)"/>
          <rect x="4" y="6" width="12" height="8" fill="none" stroke="var(--icon-fg)" stroke-width="1.4"/>
          <path d="M4 6 L10 11 L16 6" fill="none" stroke="var(--icon-fg)" stroke-width="1.4"/>
        </svg>
        <span>dale@ventureharbor.example.au</span>
      </div>
      <div class="contact-row">
        <svg class="contact-icon" viewBox="0 0 20 20" aria-hidden="true">
          <rect width="20" height="20" fill="var(--brand-blue)"/>
          <rect x="6" y="6" width="8" height="8" fill="var(--icon-fg)"/>
        </svg>
        <span>dalewhitfordnorth</span>
      </div>
    </div>

    <div class="brand">
      <div class="brand-mark"></div>
      <div class="brand-name">Venture Harbor</div>
    </div>

    <div class="band"></div>
  </div>
</body>
</html>
```